Angebotsflyer Velia Cosmetics
Zielgruppe
Kosmetikstudio, Einzelfirma Inhabergeführt
Klientel: Damen 30+ jährig
Naturkosmetik, keine apparative Kosmetik
Aufgabenstellung
Logo und Flyer (Eröffnung) im Anhang wurden bereits über Musterbogen.de gestaltet. Aus unserer Sicht schöne Vorlage.
Geforderter Leistungsumfang:
1. Flyer 3-seitig, DIN Lang (Hochformat). Angebotsflyer Velia Cosmetics. Idee gemäss Anhang, Aussenseiten schwarz, Innenseiten weiss (bessere Lesbarkeit). TEXT gemäss Anhang.
2. Flyer 1-seitig, DIN Lang (Hochformat). Kunden werben für Kunden. Dieser Flyer kann dem Angebotsflyer als Einlage mitgegeben werden und soll natürlich dem ähnlichen Stil des Angebotsflyers entsprechen. Ideen gemäss Anhang. Keine TEXT-Vorgabe im Anhang, kann durch Designer gestaltet werden. Als Prämie werden 15 CHF + 15 CHF auf die nächste Gesichtsbehandlung vergütet.

```html
<!DOCTYPE html>
<html lang="de">
<head>
<meta charset="utf-8">
<title>Angebotsflyer Velia Cosmetics</title>
<link href="https://fonts.googleapis.com/css2?family=Montserrat:wght@400;500;600&display=swap" rel="stylesheet">
<style>
  :root {
    --page-bg: #ececec;
    --paper: #ffffff;
    --gold: #b8925f;
    --gold-light: #e9cf9c;
    --ink: #2e2e2e;
    --dark: #333230;
    --light-text: #f1f1f1;
  }
  * { margin: 0; padding: 0; box-sizing: border-box; }
  html, body { width: 1200px; height: 883px; overflow: hidden; }
  body {
    background: var(--page-bg);
    font-family: "Montserrat", Arial, sans-serif;
    color: var(--ink);
    display: flex;
    align-items: center;
    justify-content: center;
  }
  .flyer { display: flex; width: 754px; height: 800px; box-shadow: 0 6px 24px rgba(0,0,0,.12); }
  .panel { position: relative; width: 377px; height: 800px; overflow: hidden; }

  /* inner page */
  .panel--inside { background: var(--paper); }
  .hero-photo {
    position: absolute; inset: 0 0 auto 0; height: 230px;
    background: linear-gradient(135deg, #6b4a3c 0%, #e8dcd3 25%, #f6f1ec 60%, #d9c1ad 100%);
  }
  .hero-band { position: absolute; top: 130px; left: 0; width: 377px; height: 120px; }
  .inside-content { position: absolute; top: 226px; left: 30px; right: 22px; }
  .section-title { font-size: 26px; font-weight: 400; color: var(--gold); letter-spacing: .5px; line-height: 1.25; }
  .intro { font-size: 12px; margin-top: 10px; }
  .service { display: flex; align-items: center; gap: 30px; margin-top: 16px; }
  .service-photo { width: 80px; height: 80px; border-radius: 50%; border: 2px solid var(--gold); flex-shrink: 0; }
  .service-photo--face { background: radial-gradient(circle at 50% 45%, #e9c9b3 0%, #d6b09a 40%, #f3ece7 75%); }
  .service-photo--brows { background: radial-gradient(circle at 50% 55%, #d9a68a 0%, #b98366 55%, #8a5a43 100%); }
  .service-name { font-size: 17px; font-weight: 400; color: var(--gold); line-height: 1.15; }
  .checklist { list-style: none; margin-top: 14px; font-size: 12.5px; line-height: 1.3; }
  .checklist li { position: relative; padding-left: 24px; margin-bottom: 5px; }
  .checklist svg { position: absolute; left: 0; top: 3px; }
  .body-text { font-size: 12.5px; line-height: 1.5; margin-top: 16px; hyphens: auto; -webkit-hyphens: auto; }

  /* cover */
  .panel--cover { background: var(--dark); }
  .cover-photo {
    position: absolute; inset: 0 0 auto 0; height: 620px;
    background: linear-gradient(110deg, #eef0ea 0%, #f4f1f2 35%, #e6d8d0 60%, #d4a58b 80%, #c58f74 100%);
  }
  .cover-band { position: absolute; top: 0; left: 0; width: 377px; height: 800px; }
  .cta { position: absolute; top: 615px; left: 30px; font-size: 13px; font-weight: 500; color: var(--ink); transform: rotate(4.5deg); transform-origin: left; }
  .hours { position: absolute; top: 700px; left: 30px; right: 28px; color: var(--light-text); }
  .hours-title { display: flex; align-items: center; gap: 14px; font-size: 14px; font-weight: 400; color: var(--gold); }
  .hours-text { font-size: 12.5px; line-height: 1.6; margin-top: 12px; }
</style>
</head>
<body>
  <main class="flyer">
    <section class="panel panel--inside">
      <div class="hero-photo" role="img" aria-label="Foto: Gesichtsbehandlung mit weisser Maske im Kosmetikstudio"></div>
      <svg class="hero-band" viewBox="0 0 377 120" aria-hidden="true">
        <defs>
          <linearGradient id="goldFade" x1="0" x2="1">
            <stop offset="0" stop-color="#f1dcac"/>
            <stop offset="1" stop-color="#c29a67"/>
          </linearGradient>
        </defs>
        <polygon points="0,25 377,110 377,120 0,120" fill="url(#goldFade)"/>
        <polygon points="0,55 377,120 0,120" fill="#ffffff"/>
      </svg>
      <div class="inside-content">
        <h2 class="section-title">Behandlungen</h2>
        <p class="intro">Folgende Behandlungen biete ich Ihnen gerne an:</p>
        <div class="service">
          <div class="service-photo service-photo--face" role="img" aria-label="Foto: Porträt einer Frau bei der Gesichtspflege"></div>
          <h3 class="service-name">Gesichtspflege<br>by LUMARA</h3>
        </div>
        <ul class="checklist">
          <li><svg width="13" height="10" viewBox="0 0 13 10"><path d="M1 5l4 4 7-8" fill="none" stroke="#b8925f" stroke-width="1.5"/></svg>Wohlfühlgesichtsbehandlung –<br>mit speziellem Fussritual</li>
          <li><svg width="13" height="10" viewBox="0 0 13 10"><path d="M1 5l4 4 7-8" fill="none" stroke="#b8925f" stroke-width="1.5"/></svg>Klassische Gesichtsbehandlung –<br>perfekt auf Ihren Hauttyp abgestimmt</li>
          <li><svg width="13" height="10" viewBox="0 0 13 10"><path d="M1 5l4 4 7-8" fill="none" stroke="#b8925f" stroke-width="1.5"/></svg>Straffende Anti-Aging Gesichtsbehandlung</li>
          <li><svg width="13" height="10" viewBox="0 0 13 10"><path d="M1 5l4 4 7-8" fill="none" stroke="#b8925f" stroke-width="1.5"/></svg>Kurze Gesichtsbehandlung</li>
          <li><svg width="13" height="10" viewBox="0 0 13 10"><path d="M1 5l4 4 7-8" fill="none" stroke="#b8925f" stroke-width="1.5"/></svg>Gentleman’s Corner – einfach entspannen!</li>
        </ul>
        <div class="service">
          <div class="service-photo service-photo--brows" role="img" aria-label="Foto: Auge mit gefärbten Wimpern und Augenbrauen"></div>
          <h3 class="service-name">Wimpern- und<br>Augenbrauen färben</h3>
        </div>
        <p class="body-text">Ein Muss für geheimnisvolle, elegant verführerische Blicke. Die dunkeln Wimpern sowie farblich abgestimmten Augenbrauen und Formen verleihen Ihrem Gesicht mehr Ausdruck. Wenig Aufwand – grosser Effekt.</p>
      </div>
    </section>

    <section class="panel panel--cover">
      <div class="cover-photo" role="img" aria-label="Foto: Frau mit geschlossenen Augen neben weissen Kirschblüten"></div>
      <svg class="cover-band" viewBox="0 0 377 800" aria-hidden="true">
        <polygon points="0,580 377,620 377,680 0,640" fill="#b8925f"/>
        <polygon points="0,640 377,680 377,800 0,800" fill="#333230"/>
      </svg>
      <p class="cta">Jetzt Zeit zum geniessen buchen!</p>
      <div class="hours">
        <h3 class="hours-title">
          <svg width="20" height="20" viewBox="0 0 20 20"><circle cx="10" cy="10" r="8.5" fill="none" stroke="#b8925f" stroke-width="1.3"/><path d="M10 5v5h4" fill="none" stroke="#b8925f" stroke-width="1.3"/></svg>
          Öffnungszeiten
        </h3>
        <p class="hours-text">Termine nach Vereinbarung. Bitte rufen Sie mich an oder senden Sie Ihren Wunschtermin per Kontaktformular oder E-Mail.</p>
      </div>
    </section>
  </main>
</body>
</html>
```